Business Card Design

I want to pull elements/colors from Website. Attached is a screen shot. Do not want any buildings/building graphics/construction clichés. This is for a construction management firm but I want to keep it broad enough that I can expand into other areas. I do not want the logo to be limited. Thank you.
Updates

Please review the screen shot of the website. Please use the font and color of Brackwell Holdings, LLC on the website. Please use the tag line "Construction Management in the Palm Beaches" Please show contractor license ... CGC 7309462 You may use the back for the contact information. Please no phone/house icons. It does not have to be a black card. Thank you.

Target Market(s)

Professional people with money. Owners, Architects, Engineers, Developers, Real Estate Agents etc.

Industry/Entity Type

Construction

Contact Information for Business Card

Brackwell Holdings, LLC
Construction Management

Dale T Brackwell
482 Osterly Court #19
North Palm Beach, FL 33999
(555) 247-3806
www.BrackwellHoldings.example

Requirements
Must have
• Clean, crisp, modern.

Broad enough that it is not trapped into a particular industry.

My goal is to expand into different markets, different industries.

Should not have
• The back of the card should not be colored in any way. Rubs off on other cards.

Do not want any buildings/building graphics/construction clichés.

```html
<!DOCTYPE html>
<html lang="en">
<head>
<meta charset="utf-8">
<title>Brackwell Holdings — Business Card</title>
<link href="https://fonts.googleapis.com/css2?family=Fira+Sans:wght@300;400;600&display=swap" rel="stylesheet">
<style>
  :root {
    --backdrop: #2a2a2a;
    --card: #f7f7f5;
    --band: #231f20;
    --tab: #4a4341;
    --band-text: #f2f2f2;
    --band-sub: #d6d6d6;
    --body-text: #2b2b2b;
  }
  html, body {
    margin: 0;
    width: 1200px;
    height: 1000px;
    overflow: hidden;
    background: var(--backdrop);
    font-family: "Fira Sans", Arial, sans-serif;
  }
  .stage {
    width: 1200px;
    height: 1000px;
    display: flex;
    align-items: center;
    justify-content: center;
  }
  .card {
    position: relative;
    width: 840px;
    height: 480px;
    background: var(--card);
    box-shadow: 0 12px 30px rgba(0,0,0,.45);
  }
  .tab { position: absolute; background: var(--tab); }
  .tab--left { left: 0; top: 0; width: 44px; height: 34px; }
  .tab--right { right: 0; top: 184px; width: 66px; height: 52px; }
  .band {
    position: absolute;
    left: 44px;
    top: 34px;
    width: 730px;
    height: 202px;
    background: linear-gradient(180deg, #2c2728 0%, var(--band) 100%);
    box-sizing: border-box;
    padding: 40px 0 0 64px;
  }
  .band__name {
    margin: 0;
    color: var(--band-text);
    font-weight: 600;
    font-size: 58px;
    line-height: 1.05;
    letter-spacing: -0.5px;
  }
  .band__tagline {
    margin: 14px 0 0;
    color: var(--band-sub);
    font-weight: 300;
    font-size: 25px;
    letter-spacing: 0.2px;
  }
  .details {
    position: absolute;
    left: 44px;
    top: 268px;
    width: 720px;
    color: var(--body-text);
    font-size: 17px;
    line-height: 1.45;
  }
  .details p { margin: 0; }
  .details strong { font-weight: 600; }
  .details .phone { font-weight: 600; font-size: 18px; }
  .details .license { margin-top: 6px; }
  .website {
    position: absolute;
    left: 330px;
    top: 410px;
    color: var(--body-text);
    font-size: 18px;
  }
</style>
</head>
<body>
<main class="stage">
  <article class="card">
    <span class="tab tab--left"></span>
    <span class="tab tab--right"></span>
    <header class="band">
      <h1 class="band__name">Brackwell Holdings</h1>
      <p class="band__tagline">Construction Management in the Palm Beaches</p>
    </header>
    <section class="details">
      <p><strong>Brackwell Holdings</strong>, LLC Construction Management Dale T Brackwell</p>
      <p>482 Osterly Court #19 North Palm Beach, FL 33999</p>
      <p class="phone">(555) 247-3806</p>
      <p class="license">Contractor License <strong>CGC 7309462</strong></p>
    </section>
    <p class="website">www.BrackwellHoldings.example</p>
  </article>
</main>
</body>
</html>
```